Business Card design + business logo for email

My company is called Harbour Cellars. I will be selling a range of beverages from wine, spirits, craft beer to cider. I would like the feel to be like I care about my customers business. My strength is tailoring/offering products that I know will suit their outlet & area demographic. I value strong, genuine relationships with my customers I service. Please ring me on 0471263958 for any further info you may need to get the right result.

```html
<!DOCTYPE html>
<html lang="en">
<head>
<meta charset="utf-8">
<title>Harbour Cellars – Business Card</title>
<link rel="stylesheet" href="https://fonts.googleapis.com/css2?family=Open+Sans:wght@400;600&display=swap">
<style>
  :root {
    --page-bg: #ffffff;
    --card-bg: #000000;
    --gold: #f8b418;
    --stripe-start: #f47a20;
    --stripe-end: #fff200;
    --text-light: #ffffff;
  }
  html, body {
    margin: 0;
    padding: 0;
    width: 1200px;
    height: 1200px;
    overflow: hidden;
    background: var(--page-bg);
    font-family: "Open Sans", Arial, sans-serif;
  }
  .canvas {
    position: relative;
    width: 1200px;
    height: 1200px;
  }
  .card {
    position: absolute;
    left: 255px;
    width: 700px;
    height: 400px;
    background: var(--card-bg);
    overflow: hidden;
  }
  .card--front { top: 145px; }
  .card--back { top: 599px; }

  .brand-ring {
    position: absolute;
    display: block;
  }
  .card--front .brand-ring {
    left: 289px;
    top: 89px;
  }
  .brand-name {
    position: absolute;
    left: 0;
    width: 100%;
    top: 218px;
    margin: 0;
    text-align: center;
    font-weight: 400;
    font-size: 40px;
    letter-spacing: 0.5px;
    color: var(--gold);
  }

  .card--back .brand-ring {
    left: 26px;
    top: 95px;
  }
  .brand-name--mark {
    position: absolute;
    left: 26px;
    top: 180px;
    width: 206px;
    margin: 0;
    text-align: center;
    font-weight: 400;
    font-size: 23px;
    color: var(--gold);
  }
  .contact-name {
    position: absolute;
    left: 248px;
    width: 400px;
    top: 68px;
    margin: 0;
    text-align: center;
    font-weight: 400;
    font-size: 38px;
    color: var(--text-light);
  }
  .contact-details {
    position: absolute;
    left: 150px;
    width: 600px;
    top: 273px;
    margin: 0;
    text-align: center;
    font-size: 22px;
    line-height: 34px;
    color: var(--text-light);
    font-style: normal;
  }
  .contact-details span { display: block; }
  .contact-details .phone { padding-left: 28px; }
  .accent-stripe {
    position: absolute;
    left: 0;
    top: 360px;
    width: 100%;
    height: 9px;
    background: linear-gradient(90deg, var(--stripe-start), var(--stripe-end));
  }
</style>
</head>
<body>
<main class="canvas">
  <section class="card card--front">
    <svg class="brand-ring" width="100" height="100" viewBox="0 0 100 100" aria-hidden="true">
      <circle cx="50" cy="50" r="46" fill="none" stroke="var(--gold)" stroke-width="5"/>
    </svg>
    <h1 class="brand-name">Harbour Cellars</h1>
  </section>

  <section class="card card--back">
    <svg class="brand-ring" width="206" height="206" viewBox="0 0 206 206" aria-hidden="true">
      <circle cx="103" cy="103" r="97" fill="none" stroke="var(--gold)" stroke-width="8"/>
    </svg>
    <p class="brand-name--mark">Harbour Cellars</p>
    <h2 class="contact-name">Liam Ostrander</h2>
    <address class="contact-details">
      <span class="phone">m 000 000 000</span>
      <span class="address">48 quay street porttown 204519</span>
    </address>
    <div class="accent-stripe"></div>
  </section>
</main>
</body>
</html>
```